Psychotherapy Practice Needs Non-Corporate Stationary

I need an elegant design for letterhead, envelope, and note card for my psychotherapy private practice in Silicon Valley. I work with pre-teens, teens, and adults primarily with anxiety, stress, and depression.

Stationary should convey warmth and professionalism. I tend to like somewhat modern designs.

My business card is already done--attached here for reference.

Target Market(s)

Professionals of Silicon Valley, Academic Advisors at High Schools, Psychologists, Psychiatrists, Pediatricians, Directors of Human Resources, Community leaders

Industry/Entity Type

Psychology

Font styles to use
Serif

Requirements
Must have
• Logo attached--can use with or without the name included. Feel free to move the name to the right of the logo. I included all versions just in case. Colors to use should match or go with the logo (greens, maybe blues if they go), but can be somewhat softer than the bold greens and browns used. (Ex. more sage green vs. kelly green)
• Letterhead--please include the following:
• Celia Montvale, LMFT
• 512 Birchwood Lane, Suite 41
• Larkspur Hills, CA 95990
• 650-381-7026
• celia@celiamontvale.example
• celiamontvale.example
• Envelope--please include:
• Celia Montvale, LMFT
• Larkspur Hills, CA 95990
• 650-381-7026
• celiamontvale.example
• Note Card--please include:
• Celia Montvale, LMFT
• 650-381-7026
• celiamontvale.example
Nice to have
• I'd love to see examples both with and without a logo watermark in the background. I especially like the watermark towards the lower right corner for the letterhead. I'd also like to see some versions of the letterhead with all contact info at the bottom.
Should not have
• It should not be corporate and should avoid harsh lines.

```html
<!DOCTYPE html>
<html lang="en">
<head>
<meta charset="utf-8">
<title>Celia Montvale, LMFT — Stationery</title>
<link rel="stylesheet" href="https://fonts.googleapis.com/css2?family=Cinzel:wght@400&family=Open+Sans:wght@400;700&display=swap">
<style>
  :root {
    --backdrop: #7d7d7d;
    --paper: #efefef;
    --leaf: #76a53e;
    --ink: #3a3a3a;
    --ink-soft: #555555;
    --window: #a9a9a9;
    --fold: #c9c9c9;
  }
  * { box-sizing: border-box; margin: 0; padding: 0; }
  html, body {
    width: 1200px; height: 800px; overflow: hidden;
    background: var(--backdrop);
  }
  .canvas { position: relative; width: 1200px; height: 800px; }

  .sheet { position: absolute; background: var(--paper); }

  /* Window envelope, front */
  .envelope-front { left: 277px; top: 65px; width: 380px; height: 193px; }
  .envelope-front .accent-bar {
    position: absolute; left: 0; top: 34px; width: 7px; height: 54px; background: var(--leaf);
  }
  .envelope-front .brand { position: absolute; left: 18px; top: 34px; text-align center; text-align: center; }
  .envelope-front .window {
    position: absolute; left: 213px; top: 70px; width: 149px; height: 72px;
    background: var(--window); border: 1px solid #8e8e8e; border-radius: 5px;
  }

  .brand-dot { display: block; margin: 0 auto 6px; border-radius: 50%; background: var(--leaf); }
  .brand-name {
    font-family: "Cinzel", Georgia, serif; color: var(--ink); white-space: nowrap; letter-spacing: 0.02em;
  }
  .envelope-front .brand-dot { width: 30px; height: 30px; }
  .envelope-front .brand-name { font-size: 8.5px; }

  /* Envelope, back */
  .envelope-back { left: 721px; top: 62px; width: 393px; height: 196px; overflow: hidden; }
  .envelope-back .flap { position: absolute; left: 0; top: 0; width: 393px; height: 80px; }
  .contact { position: absolute; font-family: "Open Sans", Arial, sans-serif; color: var(--ink-soft); white-space: nowrap; }
  .contact-title { font-weight: 700; color: var(--ink); letter-spacing: 0.01em; }
  .contact-title .given { color: var(--leaf); }
  .contact-line { display: flex; align-items: center; gap: 5px; }
  .contact-line svg { flex: none; }
  .envelope-back .contact { left: 12px; top: 139px; font-size: 6.5px; line-height: 11.5px; }
  .envelope-back .contact-title { font-size: 7px; margin-bottom: 3px; }

  /* Presentation folder, opened flat */
  .folder { position: absolute; left: 60px; top: 300px; width: 840px; height: 466px; }
  .folder-panel { position: absolute; top: 0; width: 420px; height: 466px; background: var(--paper); }
  .folder-panel.inside { left: 0; }
  .folder-panel.cover { left: 420px; border-left: 1px solid var(--fold); }

  .folder-panel.inside .contact { left: 22px; top: 272px; font-size: 6.5px; line-height: 11px; }
  .folder-panel.inside .contact-title { font-size: 7px; margin-bottom: 2px; }
  .folder-panel.inside .address { padding-left: 12px; }

  .cover .brand { position: absolute; left: 0; right: 0; top: 212px; text-align: center; padding-left: 80px; }
  .cover .brand-dot { width: 62px; height: 62px; margin-bottom: 10px; }
  .cover .brand-name { font-size: 14px; }
  .cover .accent-tab {
    position: absolute; right: 0; top: 212px; width: 8px; height: 98px; background: var(--leaf);
  }
  .cover .web-address {
    position: absolute; left: 0; right: 0; bottom: 32px; text-align: center;
    font-family: "Open Sans", Arial, sans-serif; font-size: 8.5px; letter-spacing: 0.06em; color: var(--ink);
  }
</style>
</head>
<body>
<main class="canvas">

  <section class="sheet envelope-front" aria-label="Window envelope, front">
    <div class="accent-bar"></div>
    <div class="brand">
      <span class="brand-dot"></span>
      <span class="brand-name">Celia Montvale, LMFT</span>
    </div>
    <div class="window"></div>
  </section>

  <section class="sheet envelope-back" aria-label="Envelope, back">
    <svg class="flap" viewBox="0 0 393 80" preserveAspectRatio="none" aria-hidden="true">
      <path d="M0 0 H393 V10 Q393 18 384 20 L214 74 Q200 78 186 74 L9 20 Q0 18 0 10 Z" fill="var(--leaf)"/>
    </svg>
    <div class="contact">
      <p class="contact-title"><span class="given">CELIA MONTVALE</span>, LMFT</p>
      <p class="contact-line">
        <svg width="7" height="7" viewBox="0 0 10 10" aria-hidden="true"><path d="M2 1 L4 1 L5 3.5 L3.8 4.6 Q5 6.6 6.4 6.9 L7.5 5.8 L9.5 7 V9 Q5 9.5 2.3 6 Q0.6 3.5 2 1 Z" fill="var(--leaf)"/></svg>
        650-381-7026</p>
      <p class="contact-line">
        <svg width="7" height="7" viewBox="0 0 10 10" aria-hidden="true"><circle cx="5" cy="5" r="4" fill="none" stroke="var(--leaf)" stroke-width="1.2"/><path d="M1 5 H9 M5 1 Q2.5 5 5 9 Q7.5 5 5 1" fill="none" stroke="var(--leaf)" stroke-width="0.9"/></svg>
        celiamontvale.example</p>
      <p class="contact-line">
        <svg width="7" height="7" viewBox="0 0 10 10" aria-hidden="true"><rect x="1" y="2.5" width="8" height="5.5" fill="none" stroke="var(--leaf)" stroke-width="1.1"/><path d="M1 2.5 L5 6 L9 2.5" fill="none" stroke="var(--leaf)" stroke-width="1"/></svg>
        celia@celiamontvale.example</p>
    </div>
  </section>

  <section class="folder" aria-label="Presentation folder, opened">
    <div class="folder-panel inside">
      <div class="contact">
        <p class="contact-title"><span class="given">CELIA MONTVALE</span>, LMFT</p>
        <p class="contact-line">
          <svg width="7" height="7" viewBox="0 0 10 10" aria-hidden="true"><path d="M5 0.8 Q8.3 0.8 8.3 4 Q8.3 6 5 9.5 Q1.7 6 1.7 4 Q1.7 0.8 5 0.8 Z" fill="var(--leaf)"/><circle cx="5" cy="4" r="1.3" fill="var(--paper)"/></svg>
          512 Birchwood Lane, Suite 41</p>
        <p class="address">Larkspur Hills, CA 95990</p>
        <p class="contact-line">
          <svg width="7" height="7" viewBox="0 0 10 10" aria-hidden="true"><path d="M2 1 L4 1 L5 3.5 L3.8 4.6 Q5 6.6 6.4 6.9 L7.5 5.8 L9.5 7 V9 Q5 9.5 2.3 6 Q0.6 3.5 2 1 Z" fill="var(--leaf)"/></svg>
          650-381-7026</p>
        <p class="contact-line">
          <svg width="7" height="7" viewBox="0 0 10 10" aria-hidden="true"><circle cx="5" cy="5" r="4" fill="none" stroke="var(--leaf)" stroke-width="1.2"/><path d="M1 5 H9 M5 1 Q2.5 5 5 9 Q7.5 5 5 1" fill="none" stroke="var(--leaf)" stroke-width="0.9"/></svg>
          celiamontvale.example</p>
        <p class="contact-line">
          <svg width="7" height="7" viewBox="0 0 10 10" aria-hidden="true"><rect x="1" y="2.5" width="8" height="5.5" fill="none" stroke="var(--leaf)" stroke-width="1.1"/><path d="M1 2.5 L5 6 L9 2.5" fill="none" stroke="var(--leaf)" stroke-width="1"/></svg>
          celia@celiamontvale.example</p>
      </div>
    </div>
    <div class="folder-panel cover">
      <div class="brand">
        <span class="brand-dot"></span>
        <span class="brand-name">Celia Montvale, LMFT</span>
      </div>
      <div class="accent-tab"></div>
      <p class="web-address">CELIAMONTVALE.EXAMPLE</p>
    </div>
  </section>

</main>
</body>
</html>
```